Business Card for KV

We need a double sided business card:

First Name Last Name
Cell 987-605-3214
mailbox@pelvaro-post.com

License #8096-WXYZ-2318
WFLMA # 60782
Hollin County

```html
<!DOCTYPE html>
<html lang="en">
<head>
<meta charset="utf-8">
<title>Kovara Valley — Business Card</title>
<link rel="stylesheet" href="https://fonts.googleapis.com/css2?family=Montserrat:wght@400;700&display=swap">
<style>
  :root {
    --navy: #2e5170;
    --olive: #9a9a3a;
    --paper: #f6f6f6;
    --ink: #4a4a4a;
    --backdrop: #d9d9d9;
  }
  * { margin: 0; padding: 0; box-sizing: border-box; }
  html, body { width: 1200px; height: 884px; overflow: hidden; }
  body {
    background: var(--backdrop);
    font-family: "Montserrat", sans-serif;
    display: flex;
    flex-direction: column;
    align-items: center;
    justify-content: center;
    gap: 48px;
  }
  .card {
    width: 620px;
    height: 354px;
    border-bottom: 3px solid var(--olive);
    box-shadow: 0 8px 20px rgba(0,0,0,0.18);
    position: relative;
    display: flex;
    align-items: center;
  }
  .card-front { background: var(--paper); padding: 0 36px; justify-content: space-between; }
  .card-back { background: var(--navy); justify-content: center; }

  .brand {
    display: flex;
    align-items: center;
    gap: 12px;
    flex: 0 0 auto;
  }
  .brand-dot {
    width: 28px; height: 28px;
    border-radius: 50%;
    background: var(--olive);
  }
  .brand-name {
    font-weight: 700;
    font-size: 24px;
    letter-spacing: 1px;
    text-transform: uppercase;
    color: var(--navy);
    white-space: nowrap;
  }
  .card-back .brand-dot { width: 48px; height: 48px; }
  .card-back .brand-name { font-size: 42px; color: #f2f2f2; letter-spacing: 2px; }

  .contact {
    color: var(--ink);
    font-size: 14px;
    line-height: 1.4;
    white-space: nowrap;
    flex: 0 0 auto;
  }
  .contact-name {
    color: var(--navy);
    font-weight: 700;
    font-size: 18px;
    text-transform: uppercase;
  }
  .contact-title { margin-bottom: 8px; }
  .contact-label { color: var(--navy); font-weight: 700; }
</style>
</head>
<body>
  <section class="card card-front">
    <div class="brand">
      <span class="brand-dot"></span>
      <span class="brand-name">Kovara Valley</span>
    </div>
    <div class="contact">
      <p class="contact-name">Marin Tollek</p>
      <p class="contact-title">Managing Director</p>
      <p><span class="contact-label">T.</span> 987-605-3214</p>
      <p><span class="contact-label">E.</span> mailbox@pelvaro-post.com</p>
      <p>License #8096-WXYZ-2318</p>
      <p>WFLMA # 60782</p>
      <p>Hollin County</p>
    </div>
  </section>

  <section class="card card-back">
    <div class="brand">
      <span class="brand-dot"></span>
      <span class="brand-name">Kovara Valley</span>
    </div>
  </section>
</body>
</html>
```